We need a home page that represents us as the best Veterinary Hospital in the State

We need webdesign for a Vet Hospital in Rio de Janeiro, Brazil.
We think the current design is very childish. We want something that looks more like a hospital and not a clinic.
We put a map to guide the content of the sections and also an example of a layout that we don't like but that may serve as a reference as a wireframe.

Target Market(s)

pet owners

Industry/Entity Type

Pet Care

Number of Pages Required

1 page

Requirements
Must have
• Here is a map of the sections and texts we think for home: https://qx.vz/5719382046?t=PlorvKanbe
Nice to have
• some sites we like:
https://www.valtorim.br/Pages/Home.aspx
https://www.pelmarvito.com/
Should not have
• This is a design that we started working on and the content is correct. But the layout is poor in detail, bad colors, CTA's without prominence.

https://ronalbekwistudio.plotvarex.com/console/share/KT7N9H2WRM/918273645

```html
<!DOCTYPE html>
<html lang="pt-BR">
<head>
<meta charset="utf-8">
<title>VETRA 24h – Hospital Veterinário</title>
<link href="https://fonts.googleapis.com/css2?family=Poppins:wght@400;500;600;700&display=swap" rel="stylesheet">
<style>
:root{
  --blue:#1466b8;
  --blue-dark:#0f559d;
  --red:#c8102e;
  --ink:#1d1d1b;
  --muted:#555;
  --light:#f4f4f4;
  --navy:#33465e;
  --white:#fff;
}
*{box-sizing:border-box;margin:0;padding:0}
html,body{width:1200px;height:3471px;overflow:hidden;font-family:'Poppins',sans-serif;color:var(--ink);background:#fff}
.page{position:relative;width:1200px;height:3471px}
a{color:inherit;text-decoration:none}
.btn{display:inline-flex;align-items:center;gap:8px;background:var(--red);color:#fff;font-size:12px;font-weight:600;letter-spacing:.5px;padding:7px 16px;border-radius:2px;text-transform:uppercase}
.btn svg{width:8px;height:10px}

/* hero */
.hero{position:absolute;top:0;left:0;width:1200px;height:650px;overflow:hidden}
.hero-photo{position:absolute;inset:0;background:linear-gradient(100deg,#3d6fa6 0%,#7ea5cc 35%,#c9b7a3 60%,#a9c1dd 80%,#6b90c0 100%)}
.hero-shade{position:absolute;inset:0;background:linear-gradient(90deg,rgba(20,50,90,.55),rgba(20,50,90,0) 60%)}
.topbar{position:absolute;top:14px;left:58px;right:58px;display:flex;justify-content:space-between;color:#fff;font-size:12px;font-weight:500}
.topbar span{display:flex;align-items:center;gap:8px}
.topbar svg{width:14px;height:14px}
.header{position:absolute;top:50px;left:33px;width:1134px;height:66px;background:#fff;display:flex;align-items:center;padding:0 30px}
.logo{display:flex;align-items:center;gap:8px;font-weight:700;font-size:24px;color:var(--blue)}
.logo i{width:18px;height:18px;background:var(--red);display:block}
.nav{display:flex;gap:22px;margin-left:100px;font-size:12px;font-weight:500}
.nav a.active{color:var(--blue);border-bottom:2px solid var(--blue);padding-bottom:4px}
.header .cta{margin-left:auto;background:var(--red);color:#fff;font-size:12px;font-weight:600;padding:7px 10px;border-radius:2px}
.hero-copy{position:absolute;top:235px;left:88px;color:#fff;width:420px}
.hero-copy h1{font-size:46px;font-weight:700;line-height:1.1;text-transform:uppercase}
.hero-copy .rule{width:245px;height:3px;background:#fff;margin:20px 0 14px}
.hero-copy p{font-size:18px;font-weight:500;line-height:1.35;margin-bottom:12px}

/* services */
.services{position:absolute;top:588px;left:109px;width:981px;height:120px;background:var(--blue);display:flex;align-items:center;border-radius:2px}
.service{flex:1;display:flex;flex-direction:column;align-items:center;gap:10px;color:#fff;font-size:13px;font-weight:500;border-right:1px solid rgba(255,255,255,.4);height:70px;justify-content:center}
.service:last-child{border:none}
.service svg{width:36px;height:36px;stroke:#fff;fill:none;stroke-width:1.6}

/* units */
.units{position:absolute;top:760px;left:0;width:1200px;height:588px;text-align:center}
.sec-title{font-size:30px;font-weight:600}
.dash{display:flex;justify-content:center;gap:8px;margin-top:14px}
.dash i{display:block;height:3px;background:var(--ink);width:150px}
.dash i+i{width:34px}
.cards{display:flex;justify-content:center;gap:28px;margin-top:50px;align-items:flex-start}
.card{width:292px;background:#fff;box-shadow:0 4px 16px rgba(0,0,0,.12);text-align:left}
.card.mid{width:318px;margin-top:-16px}
.card .ph{height:163px;background:linear-gradient(135deg,#c2cfd8,#d9a56a 60%,#8da3b2)}
.card.mid .ph{height:178px;background:linear-gradient(135deg,#2c9ed8,#5fc3ea 50%,#3b4a57)}
.card .body{padding:22px 26px 20px}
.card h3{font-size:17px;font-weight:600;margin-bottom:14px}
.card p{font-size:12px;line-height:1.5;color:var(--ink)}
.card .addr{font-size:11px;color:var(--muted);margin-top:8px}
.card .map{display:flex;justify-content:flex-end;align-items:center;gap:14px;font-size:11px;margin-top:22px}
.card .map svg{width:22px;height:8px}

/* infra */
.infra{position:absolute;top:1348px;left:0;width:1200px;height:472px;background:var(--light)}
.video{position:absolute;top:94px;left:69px;width:446px;height:279px;background:linear-gradient(120deg,#7c7f84,#b7b3ab 45%,#2aa6b6 85%)}
.video .play{position:absolute;top:50%;left:50%;width:40px;height:40px;margin:-20px 0 0 -20px;border-radius:50%;background:#fff;display:flex;align-items:center;justify-content:center}
.infra-copy{position:absolute;top:118px;left:560px;width:580px}
.infra-copy h2{font-size:30px;font-weight:600;line-height:1.4}
.infra-copy .dash{justify-content:flex-start;margin:10px 0 22px}
.infra-copy p{font-size:22px;font-weight:500;color:var(--blue);line-height:1.35;margin-bottom:28px}

/* testimonials */
.testi{position:absolute;top:1820px;left:0;width:1200px;height:516px;background:linear-gradient(90deg,#2e4058,#4b5f78 50%,#2e4058);color:#fff;text-align:center}
.testi .kicker{font-size:14px;margin-top:46px}
.testi h2{font-size:30px;font-weight:600;margin-top:4px}
.testi .dash i{background:#fff}
.quotes{display:flex;justify-content:center;gap:42px;margin-top:40px}
.quote{width:393px;text-align:left}
.quote .box{position:relative;background:#fff;color:var(--ink);font-size:12px;line-height:1.55;padding:24px 24px 20px}
.quote .box::after{content:"";position:absolute;bottom:-22px;left:60px;border-left:0 solid transparent;border-right:36px solid transparent;border-top:22px solid #fff}
.quote .qm{color:var(--blue);font-size:32px;font-weight:700;line-height:0;vertical-align:-12px;margin-right:6px}
.author{display:flex;align-items:center;gap:16px;margin:44px 0 0 8px;font-size:12px}
.author .av{width:46px;height:46px;border-radius:50%;background:#c9cfd6;border:3px solid #fff}
.author small{display:block;font-size:10px;opacity:.85}
.author .stars{color:#f7d21a;font-size:11px;letter-spacing:1px}
.arrow{position:absolute;top:272px;color:#fff}
.arrow svg{width:12px;height:20px;stroke:#fff;fill:none;stroke-width:2}

/* blog */
.blog{position:absolute;top:2336px;left:0;width:1200px;height:812px;background:var(--light);text-align:center}
.blog .kicker{font-size:14px;font-weight:600;color:var(--blue);margin-top:84px}
.blog h2{font-size:30px;font-weight:600;margin-top:4px}
.grid{position:absolute;top:224px;left:141px;display:grid;grid-template-columns:365px 256px 256px;gap:20px;text-align:left}
.post .ph{background:linear-gradient(135deg,#b38b62,#e3c49d 50%,#8a98a6)}
.post.big .ph{height:266px;background:linear-gradient(135deg,#3a3e44,#d9d5ce 50%,#a6522e)}
.post.sm .ph{height:130px}
.post .date{display:flex;align-items:center;gap:10px;font-size:10px;margin:10px 0 6px}
.post .date i{width:10px;height:10px;background:#8fb3dc;display:block}
.post h4{font-size:12px;font-weight:500;line-height:1.45}
.post.big h4{font-size:13px}
.post .ex{font-size:10px;color:var(--muted);line-height:1.6;margin-top:10px}
.small-stack{display:grid;grid-template-rows:1fr 1fr;gap:16px}
.blog .btn{position:absolute;top:714px;left:543px}

/* footer */
.footer{position:absolute;top:3148px;left:0;width:1200px;height:323px;background:var(--blue);color:#fff}
.f-brand{position:absolute;top:60px;left:100px;width:220px}
.f-brand .logo{color:#fff;font-size:30px}
.f-brand .logo i{background:#fff}
.f-brand p{font-size:11px;margin-top:14px;line-height:1.4}
.social{display:flex;gap:12px;margin-top:14px}
.social i{width:18px;height:18px;border-radius:50%;background:#fff;display:block}
.f-col{position:absolute;top:68px;font-size:10px;line-height:1.9}
.f-col h5{font-size:12px;font-weight:600;margin-bottom:6px;text-transform:uppercase}
.f-contact{position:absolute;top:68px;left:910px;font-size:12px}
.f-contact h5{font-size:12px;font-weight:600;margin-bottom:12px}
.f-contact div{display:flex;align-items:center;gap:14px;margin-bottom:10px}
.f-contact svg{width:14px;height:14px;fill:#fff}
.news{display:flex;margin-top:22px;margin-left:-60px}
.news span{width:230px;height:28px;background:#fff;color:#999;font-size:9px;padding:9px 8px}
.news b{background:var(--red);font-size:8px;font-weight:500;padding:10px 8px}
.f-resp{position:absolute;top:272px;left:0;width:1200px;text-align:center;font-size:11px}
.f-line{position:absolute;top:292px;left:145px;width:910px;height:1px;background:rgba(255,255,255,.5)}
.f-copy{position:absolute;top:302px;left:0;width:1200px;text-align:center;font-size:9px}
</style>
</head>
<body>
<div class="page">

  <section class="hero">
    <div class="hero-photo" role="img" aria-label="Veterinária com luvas rosa examinando um pequeno cão terrier em clínica de fundo azul"></div>
    <div class="hero-shade"></div>
    <div class="topbar">
      <span><svg viewBox="0 0 16 16" fill="none" stroke="#fff" stroke-width="1.3"><rect x="1.5" y="3.5" width="13" height="9"/><path d="M1.5 3.5l6.5 5 6.5-5"/></svg>Email Us: contato@vetra24h.com.br</span>
      <span><svg viewBox="0 0 16 16" fill="#fff"><path d="M4 1.5l2.5 3-1.5 1.5c.8 2 2.5 3.7 4.5 4.5l1.5-1.5 3 2.5-1.5 2.5C7 14 2 9 1.5 3z"/></svg>Call Us: +55 21 3184-5520</span>
    </div>
    <header class="header">
      <div class="logo"><i></i>VETRA 24h</div>
      <nav class="nav">
        <a class="active">Home</a><a>Agendamentos</a><a>Vacinas</a><a>Unidades</a><a>Blog</a><a>Trabalhe</a><a>A Vetra</a><a>Area do Tutor</a>
      </nav>
      <a class="cta">Get Appointment</a>
    </header>
    <div class="hero-copy">
      <h1>Pra cuidar<br>de quem você ama!</h1>
      <div class="rule"></div>
      <p>Excelentes médicos e infraestrutura completa por um preço que cabe no seu bolso.</p>
      <a class="btn">Veja mais <svg viewBox="0 0 8 10" fill="none" stroke="#fff" stroke-width="1.6"><path d="M2 1l4 4-4 4"/></svg></a>
    </div>
  </section>

  <div class="services">
    <div class="service"><svg viewBox="0 0 36 36"><circle cx="18" cy="10" r="6"/><path d="M7 33c0-8 5-12 11-12s11 4 11 12z"/><path d="M15 25h6M18 22v6"/></svg>Pronto-Socorro</div>
    <div class="service"><svg viewBox="0 0 36 36"><path d="M10 4v10a6 6 0 0012 0V4"/><path d="M16 20v6a6 6 0 0012 0v-4"/><circle cx="28" cy="19" r="3"/></svg>Consultas</div>
    <div class="service"><svg viewBox="0 0 36 36"><path d="M9 3h13l6 6v24H9z"/><path d="M13 14h11M13 19h11M13 24h11M13 29h7"/></svg>Resultado de Exames</div>
    <div class="service"><svg viewBox="0 0 36 36"><circle cx="18" cy="18" r="13"/><path d="M18 10v8l5 4"/></svg>Agendamento de Exames</div>
    <div class="service"><svg viewBox="0 0 36 36"><path d="M26 4l6 6M29 7l-14 14-5-5L24 2M10 16l-6 6 4 4M15 21l-3 3M4 32l6-6"/></svg>Vacinas</div>
  </div>

  <section class="units">
    <h2 class="sec-title">UNIDADES VETRA 24h</h2>
    <div class="dash"><i></i><i></i></div>
    <div class="cards">
      <article class="card">
        <div class="ph" role="img" aria-label="Veterinário examinando um cão golden retriever na unidade Taquara"></div>
        <div class="body">
          <h3>Taquara - RJ</h3>
          <p>Pronto-Socorro, Atendimento Clínico e Especialidades</p>
          <p class="addr">Rua das Acácias, 88, Taquara</p>
          <div class="map">Veja no mapa <svg viewBox="0 0 22 8" fill="none" stroke="#1466b8" stroke-width="2"><path d="M0 4h20M16 1l4 3-4 3"/></svg></div>
        </div>
      </article>
      <article class="card mid">
        <div class="ph" role="img" aria-label="Cirurgia veterinária com instrumentos sobre campo cirúrgico azul"></div>
        <div class="body">
          <h3>Flamengo - RJ</h3>
          <p>Pronto-Socorro, Atendimento Clínico e Especialidades</p>
          <p class="addr">Rua dos Ipês, 412, Flamengo</p>
          <div class="map">Veja no mapa <svg viewBox="0 0 22 8" fill="none" stroke="#1466b8" stroke-width="2"><path d="M0 4h20M16 1l4 3-4 3"/></svg></div>
        </div>
      </article>
      <article class="card">
        <div class="ph" role="img" aria-label="Veterinária auscultando um cão na unidade Copacabana"></div>
        <div class="body">
          <h3>Copacabana - RJ</h3>
          <p>Pronto-Socorro, Atendimento Clínico e Especialidades</p>
          <p class="addr">Rua das Acácias, 88, Taquara</p>
          <div class="map">Veja no mapa <svg viewBox="0 0 22 8" fill="none" stroke="#1466b8" stroke-width="2"><path d="M0 4h20M16 1l4 3-4 3"/></svg></div>
        </div>
      </article>
    </div>
  </section>

  <section class="infra">
    <div class="video" role="img" aria-label="Gato recebendo curativo na pata por mãos com luvas azuis">
      <div class="play"><svg width="14" height="16" viewBox="0 0 14 16"><path d="M2 1l11 7-11 7z" fill="#c8102e"/></svg></div>
    </div>
    <div class="infra-copy">
      <h2>Infraestrutura completa e equipe médica disponível 24h todos os dias</h2>
      <div class="dash"><i></i><i></i></div>
      <p>Pronto-socorro, centro de internação,exames de imagem. cirurgia.</p>
      <a class="btn">Veja o vídeo <svg viewBox="0 0 8 10" fill="none" stroke="#fff" stroke-width="1.6"><path d="M2 1l4 4-4 4"/></svg></a>
    </div>
  </section>

  <section class="testi">
    <p class="kicker">O que dizem alguns tutores</p>
    <h2>Pegar testemunhos Perfil da Empresa</h2>
    <div class="dash"><i></i><i></i></div>
    <span class="arrow" style="left:372px"><svg viewBox="0 0 12 20"><path d="M10 2L2 10l8 8"/></svg></span>
    <span class="arrow" style="left:1312px;left:1312px"></span>
    <span class="arrow" style="left:1314px"></span>
    <span class="arrow" style="left:1310px"></span>
    <span class="arrow" style="left:1311px"></span>
    <span class="arrow" style="right:126px"><svg viewBox="0 0 12 20"><path d="M2 2l8 8-8 8"/></svg></span>
    <div class="quotes">
      <div class="quote">
        <div class="box"><span class="qm">“</span>Lorem ipsum dolor sit amet, consetetur sadipscing elitr, sed diam nonumy eirmod tempor invidunt ut labore et dolore magna aliquyam erat, sed diam voluptua. At vero eos et accusam et justo duo dolores et ea rebum. Stet clita kasd gubergren, no sea takimata sanctus est Lorem ipsum dolor sit amet.</div>
        <div class="author"><span class="av"></span><div>Lorem ipsum<small>dolor sit amet,</small><span class="stars">★★★★★</span></div></div>
      </div>
      <div class="quote">
        <div class="box"><span class="qm">“</span>Lorem ipsum dolor sit amet, consetetur sadipscing elitr, sed diam nonumy eirmod tempor invidunt ut labore et dolore magna aliquyam erat, sed diam voluptua. At vero eos et accusam et justo duo dolores et ea rebum. Stet clita kasd gubergren, no sea takimata sanctus est Lorem ipsum dolor sit amet.</div>
        <div class="author"><span class="av"></span><div>Lorem ipsum<small>dolor sit amet,</small><span class="stars">★★★★★</span></div></div>
      </div>
    </div>
  </section>

  <section class="blog">
    <p class="kicker">Você pode se interessa por</p>
    <h2>Último artigo do blog</h2>
    <div class="dash"><i></i><i></i></div>
    <div class="grid">
      <article class="post big">
        <div class="ph" role="img" aria-label="Veterinário examinando a boca de um gato com estetoscópio vermelho"></div>
        <div class="date"><i></i>22 MAY 2021</div>
        <h4>Lorem ipsum dolor sit amg hdy aeet, consete gj hur sadipscing elitr, sed diam nonumy empor</h4>
        <p class="ex">Lorem ipsum dolor sit amg hdy aeet, consete gj gdywdf thur sadipscing elitr, sed diam nonumy eirmpgh fudyru ygurdt or invidunt ut labore et dolore magna aliquyam erat, sed diam voluptua. At vero eos et accusam et justo duo dolores et ea</p>
      </article>
      <div class="small-stack">
        <article class="post sm">
          <div class="ph" role="img" aria-label="Cão sorridente deitado durante consulta"></div>
          <div class="date"><i></i>22 MAY 2021</div>
          <h4>Lorem ipsum dolor sit amg hdy aeet, consetetur sadipscing elitr, sed diam</h4>
        </article>
        <article class="post sm">
          <div class="ph" role="img" aria-label="Cão de pelo claro sendo examinado por veterinário"></div>
          <div class="date"><i></i>22 MAY 2021</div>
          <h4>Lorem ipsum dolor sit amg hdy aeet, consetetur sadipscing elitr, sed diam</h4>
        </article>
      </div>
      <div class="small-stack">
        <article class="post sm">
          <div class="ph" role="img" aria-label="Gato no colo de veterinária em consultório" style="background:linear-gradient(135deg,#2f3a4c,#c8c2ba 60%,#6c7a8c)"></div>
          <div class="date"><i></i>22 MAY 2021</div>
          <h4>Lorem ipsum dolor sit amg hdy aeet, consetetur sadipscing elitr, sed diam</h4>
        </article>
        <article class="post sm">
          <div class="ph" role="img" aria-label="Veterinária de uniforme azul segurando um gato" style="background:linear-gradient(135deg,#24406a,#8a9bb2 55%,#cfc6bb)"></div>
          <div class="date"><i></i>22 MAY 2021</div>
          <h4>Lorem ipsum dolor sit amg hdy aeet, consetetur sadipscing elitr, sed diam</h4>
        </article>
      </div>
    </div>
    <a class="btn">Leia mais <svg viewBox="0 0 8 10" fill="none" stroke="#fff" stroke-width="1.6"><path d="M2 1l4 4-4 4"/></svg></a>
  </section>

  <footer class="footer">
    <div class="f-brand">
      <div class="logo"><i></i>VETRA 24h</div>
      <p>Atendimento médico veterinário de qualidade completo e acessível.</p>
      <div class="social"><i></i><i></i><i></i><i></i></div>
    </div>
    <div class="f-col" style="left:350px"><h5>Serviços</h5>Pronto-socorro<br>Consultas<br>Exames<br>Vacinas<br>Cirurgias</div>
    <div class="f-col" style="left:500px"><h5>Vetra 24h</h5>Unidades<br>Blog<br>Trabalhe conosco<br>Quem somos</div>
    <div class="f-col" style="left:640px"><h5>Tutores</h5>Área do tutor<br>Agendamentos<br>Resultado de exames</div>
    <div class="f-col" style="left:785px"><h5>Ajuda</h5>Ouvidoria<br>Fale Conosco</div>
    <div class="f-contact">
      <h5>CENTRAL DE ATENDIMENTO</h5>
      <div><svg viewBox="0 0 16 16"><circle cx="8" cy="8" r="6.5" fill="none" stroke="#fff" stroke-width="1.4"/><path d="M5.5 5l1.5-.5 1 2-.8.8c.4.8 1 1.4 1.8 1.8l.8-.8 2 1-.5 1.5c-3 .2-6-2.8-5.8-5.8z"/></svg>+55 21 3184-5520</div>
      <div><svg viewBox="0 0 16 16"><path d="M4 1.5l2.5 3-1.5 1.5c.8 2 2.5 3.7 4.5 4.5l1.5-1.5 3 2.5-1.5 2.5C7 14 2 9 1.5 3z"/></svg>+55 21 99462-3310</div>
      <div class="news"><span>subscreva a nossa newsletter</span><b>subscrever</b></div>
    </div>
    <p class="f-resp">Responsável técnico: Dr. Marcos Albuquerque - Médico Veterinário - CRMV-RJ</p>
    <div class="f-line"></div>
    <p class="f-copy">All right reserve 2021- VETRA 24h</p>
  </footer>

</div>
</body>
</html>
```